Milo's Sweet Harbor Package Design

A logo has already been made and now i need to incorporate that logo into a package design. Milo's Sweet Harbor products will be sold in retail stores and its package should appeal to both adults and children. Milo's Sweet Harbor sells candy, nuts and other snacks. Files attached will be logo files and pictures of similar package. Please refer to the files for package design. The physical package consists of a printed card (5.75 inches X 4 inches) and a plastic bag. The card is folded over the plastic bag, sealed and hole punched. The design on the card(5.75 inches X 4 inches) should consist of the logo, price(in this case it is $1.99 however it will vary for other products) and product type (in this case its apple(however it will change for other products). On the "back side"(the card is folded down the middle over the plastic and the top of the card becomes the back side, notice how in the example the top half is upside down, this is correct) should include nutrition facts, ingredients, a UPC barcode and the company information(again these vary depending on the product except for the company information that will be same for all products. Company info - "Packaged & Distributed By: Brevik Treats Supply
7142 Larchmont Ave Suite 208 Sterling Heights, Michigan 48592 586-555-0173"

TO WHOEVER WINS THE CONTEST WE WILL COMMISSION YOU TO USE THE SAME DESIGN AND ADD THE NECESSARY INFORMATION(upc, ingredients list, nutritional facts, etc) FOR THE MULTIPLE FLAVORS THAT WE WILL BE PRODUCING UNDER THE Milo's Sweet Harbor BRAND.

```html
<!DOCTYPE html>
<html lang="en">
<head>
<meta charset="utf-8">
<title>Milo's Sweet Harbor – Apple Header Card</title>
<link href="https://fonts.googleapis.com/css2?family=Arimo:wght@400;700&family=Damion&family=Pacifico&display=swap" rel="stylesheet">
<style>
  :root{
    --sky:#56d8f4;
    --sky-light:#8fe6f8;
    --sky-deep:#1cb6e2;
    --berry:#b8334f;
    --berry-light:#d6587a;
    --royal:#0457bb;
    --cherry:#ec1c24;
    --lime:#d6f50a;
    --leaf:#4cf03a;
    --label-grey:#ececec;
    --ink:#000;
    --paper:#fff;
  }
  *{box-sizing:border-box;margin:0;padding:0}
  html,body{width:882px;height:1200px;overflow:hidden;background:var(--paper)}
  body{position:relative;font-family:Arimo,Arial,sans-serif;color:var(--ink)}
  .card{position:absolute;left:37px;top:38px;width:812px;height:1118px;background:var(--sky);overflow:hidden}

  /* back side – printed upside down */
  .back{position:absolute;left:0;top:0;width:812px;height:557px;transform:rotate(180deg)}
  .upc-panel{position:absolute;left:524px;top:424px;width:257px;height:89px;background:var(--label-grey)}
  .story{position:absolute;left:524px;top:211px;width:257px;height:195px;
    background:linear-gradient(160deg,var(--berry) 0%,var(--berry-light) 55%,var(--berry) 100%);
    padding:22px 22px;color:var(--paper);font-size:13.4px;line-height:16.5px;text-align:justify}
  .story-band{position:absolute;left:524px;top:175px;width:257px;height:36px;background:var(--royal)}
  .brand-small{position:absolute;left:558px;top:16px;width:190px;height:150px;
    display:flex;align-items:center;justify-content:center;text-align:center;
    font-family:Pacifico,cursive;font-size:32px;line-height:40px;color:var(--berry)}
  .mark{position:absolute;background:var(--ink)}
  .mark-recycle{left:315px;top:443px;width:70px;height:70px;border-radius:50%}
  .mark-dispose{left:434px;top:424px;width:53px;height:88px;border-radius:6px}

  .company{position:absolute;left:305px;top:130px;width:240px;font-size:14.5px;line-height:18px}
  .company .lead{font-weight:700;margin-bottom:10px}
  .company .made{font-weight:700;font-size:15.5px;margin-top:30px}
  .company .date{font-weight:700;font-size:11.5px;margin-top:28px}
  .company .date + .date{margin-top:28px}

  .facts-panel{position:absolute;left:29px;top:37px;width:260px;height:474px;border:2px solid var(--ink);background:var(--paper);padding:5px}
  .facts{border:1.5px solid var(--ink);padding:4px 4px 6px}
  .facts h2{font-size:25px;font-weight:700;letter-spacing:1.5px;line-height:28px}
  .facts .per{font-size:12.5px;margin-top:4px}
  .facts .size{display:flex;justify-content:space-between;font-size:14px;font-weight:700;padding-bottom:3px;border-bottom:6px solid var(--ink)}
  .facts .amount{font-size:10px;font-weight:700;margin-top:2px}
  .facts .cal{display:flex;justify-content:space-between;align-items:flex-end;font-size:22px;font-weight:700;line-height:24px;border-bottom:4px solid var(--ink);padding-bottom:2px}
  .facts .cal span:last-child{font-size:28px}
  .facts .dv{text-align:right;font-size:8.5px;font-weight:700;border-bottom:1px solid var(--ink);padding:2px 0}
  .facts .row{display:flex;justify-content:space-between;font-size:11px;line-height:15px;border-bottom:1px solid #777}
  .facts .row.sub{padding-left:12px}
  .facts .row.last{border-bottom:4px solid var(--ink)}
  .facts .note{font-size:7.5px;line-height:9.5px;padding:3px 0;border-bottom:1px solid var(--ink)}
  .facts .note + .note{border:0}
  .ingredients h3{background:var(--ink);color:var(--paper);font-size:12px;padding:4px 6px;margin-top:5px}
  .ingredients p{font-size:9.5px;line-height:12px;text-align:justify;padding:6px 5px}

  /* front side */
  .front{position:absolute;left:0;top:557px;width:812px;height:561px;
    background:radial-gradient(circle at 35% 35%,var(--sky-light) 0%,var(--sky) 70%)}
  .brand-main{position:absolute;left:46px;top:91px;width:360px;height:390px;
    display:flex;align-items:center;justify-content:center;text-align:center;
    font-family:Pacifico,cursive;font-size:60px;line-height:74px;color:var(--berry)}
  .price-shadow{position:absolute;left:537px;top:100px;width:223px;height:223px;border-radius:50%;background:var(--sky-deep)}
  .price{position:absolute;left:545px;top:88px;width:223px;height:223px;border-radius:50%;background:var(--cherry);
    display:flex;align-items:center;justify-content:center}
  .price::before{content:"";position:absolute;inset:6px;border-radius:50%;border:1.5px solid var(--paper)}
  .price .dollar{font-weight:700;font-size:92px;color:var(--lime);line-height:1}
  .price .whole{font-weight:700;font-size:96px;color:var(--paper);line-height:1}
  .price .cents{align-self:flex-start;margin-top:62px;font-weight:700;font-size:40px;color:var(--paper);border-bottom:4px solid var(--paper);line-height:1;padding-bottom:2px}
  .flavor-band{position:absolute;left:419px;top:388px;width:393px;height:112px;background:var(--leaf);border-radius:56px 0 0 56px;box-shadow:-2px 10px 0 var(--sky-deep)}
  .flavor{position:absolute;left:593px;top:400px;font-family:Damion,cursive;font-size:72px;color:var(--paper);line-height:84px}
  .apple{position:absolute;left:444px;top:310px;width:145px;height:171px}

  .hole{position:absolute;left:380px;width:48px;height:48px;border-radius:50%;background:var(--paper)}
</style>
</head>
<body>
<main class="card">
  <section class="back">
    <div class="upc-panel" aria-label="UPC label area"></div>
    <div class="story-band"></div>
    <div class="story">Lorem ipsum dolor sit amet, consectetur adipiscing elit, sed do eiusmod tempor incididunt ut labore et dolore magna aliqua. Quis ipsum suspendisse ultrices gravida. Risus commodo viverra maecenas accumsan lacus vel facilisis. Lorem ipsum dolor sit amet, consectetur adipiscing elit, sed do</div>
    <div class="brand-small">Milo's Sweet Harbor</div>

    <div class="company">
      <p class="lead">Packaged &amp; Distributed By:</p>
      <p>Brevik Treats Supply</p>
      <p>7142 Larchmont Ave</p>
      <p>Suite 208 Sterling Heights,</p>
      <p>Michigan 48592</p>
      <p>586-555-0173</p>
      <p class="made">Made in the USA</p>
      <p class="date">Manufacturing Date:</p>
      <p class="date">Expiration Date:</p>
    </div>

    <div class="mark mark-recycle" role="img" aria-label="Recycling mark"></div>
    <div class="mark mark-dispose" role="img" aria-label="Dispose of properly mark"></div>

    <div class="facts-panel">
      <div class="facts">
        <h2>Nutrition Facts</h2>
        <p class="per">6 servings per container</p>
        <div class="size"><span>Serving size</span><span>10 pcs (10g)</span></div>
        <p class="amount">Amount Per Serving</p>
        <div class="cal"><span>Calories</span><span>110</span></div>
        <p class="dv">% Daily Value*</p>
        <div class="row"><span><b>Total Fat</b> 2.5g</span><b>3%</b></div>
        <div class="row sub"><span>Saturated Fat 1g</span><b>5%</b></div>
        <div class="row sub"><span><i>Trans</i> Fat 0g</span><span></span></div>
        <div class="row"><span><b>Sodium</b> 10mg</span><b>0%</b></div>
        <div class="row"><span><b>Total Carbohydrate</b> 22g</span><b>8%</b></div>
        <div class="row sub"><span>Dietary Fiber 0g</span><b>0%</b></div>
        <div class="row sub"><span>Total Sugars 16g</span><span></span></div>
        <div class="row sub"><span>&nbsp;&nbsp;Includes 0g Added Sugars</span><b>0%</b></div>
        <div class="row last"><span><b>Protein</b> 0g</span><b>0%</b></div>
        <p class="note">Not a significant source of cholesterol, vitamin D, calcium, iron, and potassium</p>
        <p class="note">* The % Daily Value (DV) tells you how much a nutrient in a serving of food contributes to a daily diet. 2,000 calories a day is used for general nutrition advice.</p>
      </div>
      <div class="ingredients">
        <h3>Ingredients:</h3>
        <p>Lorem ipsum dolor sit amet, consectetur adipiscing elit, sed do eiusmod tempor incididunt ut labore et dolore magna aliqua. Quis ipsum suspendisse ultrices gravida. Risus commodo viverra maecenas accumsan lacus vel facilisis.</p>
      </div>
    </div>
  </section>

  <section class="front">
    <div class="brand-main">Milo's Sweet Harbor</div>
    <div class="price-shadow"></div>
    <div class="price"><span class="dollar">$</span><span class="whole">1</span><span class="cents">99</span></div>
    <div class="flavor-band"></div>
    <svg class="apple" role="img" aria-label="Illustration of a red apple with leaf" viewBox="0 0 145 171">
      <ellipse cx="68" cy="104" rx="67" ry="66" fill="#b0101a"/>
    </svg>
    <span class="flavor">Apple</span>
  </section>

  <span class="hole" style="top:461px"></span>
  <span class="hole" style="top:617px"></span>
</main>
</body>
</html>
```